Etiqueta para productos de Panaderia Serenita

Necesitamos hacer una actualizacion de nuestra etiqueta con el slogan "Tibio del Horno", les adjunto foto de la etiqueta actual y fotos de los productos en los cuales utilizamos esta etiqueta.
Somos una empresa de panaderia, ubicados en Honduras
Distribuidora Trigal SA de CV

Target Market(s)

Clientes en Supermercados

Industry/Entity Type

Panaderia

```html
<!DOCTYPE html>
<html lang="es">
<head>
<meta charset="utf-8">
<title>Etiqueta Tibio del Horno – Panaderia Serenita</title>
<link rel="stylesheet" href="https://fonts.googleapis.com/css2?family=Fredoka:wght@700&family=Oswald:wght@500&display=swap">
<style>
  :root {
    --bg: #e9e9e9;
    --gold: #d6a935;
    --gold-light: #f3d27a;
    --red: #c4141c;
    --red-dark: #8e0b10;
    --green: #1f8a3a;
    --green-dark: #0d5a24;
    --cream: #f6ecd8;
    --white: #ffffff;
  }
  * { margin: 0; padding: 0; box-sizing: border-box; }
  html, body { width: 900px; height: 1200px; overflow: hidden; background: var(--bg); }
  .label { position: relative; width: 900px; height: 1200px; }
  .label-shape { position: absolute; inset: 0; }
  .brand {
    position: absolute; left: 292px; width: 319px; top: 170px; height: 70px;
    display: flex; align-items: center; justify-content: center; gap: 12px;
  }
  .brand-dot {
    width: 18px; height: 18px; border-radius: 50%; background: var(--cream);
  }
  .brand-name {
    font-family: 'Oswald', sans-serif; font-weight: 500; font-size: 48px;
    line-height: 1; letter-spacing: 2px; color: var(--cream);
  }
  .slogan {
    position: absolute; left: 93px; width: 714px; top: 340px;
    text-align: center; font-family: 'Fredoka', sans-serif; font-weight: 700;
    font-size: 84px; line-height: 80px; color: var(--gold-light);
    text-shadow: 0 3px 0 #7a4a10, 0 5px 8px rgba(0,0,0,.45);
  }
  .claim {
    position: absolute; left: 292px; width: 319px; top: 548px;
    text-align: center; font-family: 'Oswald', sans-serif; font-weight: 500;
    font-size: 40px; line-height: 56px; letter-spacing: 1px; color: var(--white);
  }
</style>
</head>
<body>
<div class="label">
  <svg class="label-shape" width="900" height="1200" viewBox="0 0 900 1200">
    <defs>
      <clipPath id="label-clip">
        <path d="M275,105 Q275,75 305,75 H595 Q625,75 625,105 V278 H767 Q807,278 807,318 V1085 Q807,1125 767,1125 H133 Q93,1125 93,1085 V318 Q93,278 133,278 H275 Z"/>
      </clipPath>
      <radialGradient id="green-burst" cx="50%" cy="45%" r="65%">
        <stop offset="0" stop-color="#3fb04f"/>
        <stop offset="1" stop-color="#0d5a24"/>
      </radialGradient>
      <linearGradient id="red-band" x1="0" y1="0" x2="0" y2="1">
        <stop offset="0" stop-color="#8e0b10"/>
        <stop offset="0.4" stop-color="#c4141c"/>
        <stop offset="1" stop-color="#8e0b10"/>
      </linearGradient>
      <linearGradient id="gold-frame" x1="0" y1="0" x2="1" y2="1">
        <stop offset="0" stop-color="#f6dc8a"/>
        <stop offset="0.5" stop-color="#b8861f"/>
        <stop offset="1" stop-color="#f0cf6e"/>
      </linearGradient>
      <linearGradient id="pastry-tones" x1="0" y1="0" x2="1" y2="1">
        <stop offset="0" stop-color="#e2a24c"/>
        <stop offset="1" stop-color="#6b3a1c"/>
      </linearGradient>
      <linearGradient id="baker-tones" x1="0" y1="0" x2="0" y2="1">
        <stop offset="0" stop-color="#bdb3ad"/>
        <stop offset="0.4" stop-color="#d2232a"/>
        <stop offset="1" stop-color="#e8e0ea"/>
      </linearGradient>
    </defs>

    <g clip-path="url(#label-clip)">
      <rect class="side-panels" x="93" y="75" width="714" height="800" fill="url(#green-burst)"/>
      <rect class="center-band" x="292" y="75" width="319" height="800" fill="url(#red-band)"/>
      <rect class="write-in-area" x="93" y="870" width="714" height="260" fill="#ffffff"/>
    </g>

    <path class="gold-frame" d="M275,105 Q275,75 305,75 H595 Q625,75 625,105 V278 H767 Q807,278 807,318 V1085 Q807,1125 767,1125 H133 Q93,1125 93,1085 V318 Q93,278 133,278 H275 Z"
          fill="none" stroke="url(#gold-frame)" stroke-width="14"/>

    <rect class="baker-illustration" x="30" y="481" width="263" height="389" rx="20"
          fill="url(#baker-tones)" role="img" aria-label="Ilustración de una abuela panadera con delantal y batidor"/>

    <rect class="pastry-photo" x="350" y="690" width="340" height="178" rx="16"
          fill="url(#pastry-tones)" role="img" aria-label="Foto de croissants, panecillos y roles de canela sobre tablas de madera"/>

    <circle class="product-badge" cx="673" cy="607" r="64" fill="#1d1d1d" stroke="#ffffff" stroke-width="4"/>
  </svg>

  <div class="brand">
    <span class="brand-dot"></span>
    <span class="brand-name">HORNALIA</span>
  </div>
  <div class="slogan">Tibio del<br>Horno</div>
  <div class="claim">LOS MEJORES<br>INGREDIENTES</div>
</div>
</body>
</html>
```